New Wine Label - Argentinian Malbec 'Viento Callado'

I am looking for an exceptional and exciting design for a wine label called 'Viento Callado' meaning Quiet Wind or Wind of the Quiet. The design must feature the name 'Viento Callado', a star logo and the word 'Malbec'. It will also need the words 'Mendoza, Argentina' at the bottom of the label as a prominent piece of information. Please produce the work in size 80mm x 100mm. Feel free to use colour in addition to black/white and ensue that the label is easy to read on a shelf placement.

Target Market(s)

25-50 Year Olds who enjoy great wine that looks and appears interesting and a little different.

Requirements
Must have
• Star Logo
• Word - Malbec
• Words - Mendoza, Argentina
Nice to have
• Background image to label

```html
<!DOCTYPE html>
<html lang="es">
<head>
<meta charset="utf-8">
<title>Viento Callado Malbec – Label</title>
<link rel="stylesheet" href="https://fonts.googleapis.com/css2?family=Alex+Brush&display=swap">
<style>
  :root {
    --page: #ffffff;
    --night: #1c2129;
    --night-deep: #12161c;
    --night-soft: #2a3039;
    --gold: #c8912a;
    --gold-light: #e9be58;
    --gold-dark: #8c5b14;
    --ink-light: #ffffff;
    --script: "Alex Brush", cursive;
  }
  html, body {
    margin: 0;
    width: 1200px;
    height: 914px;
    overflow: hidden;
    background: var(--page);
  }
  .canvas {
    position: relative;
    width: 1200px;
    height: 914px;
  }
  .wine-label {
    position: absolute;
    left: 255px;
    top: 27px;
    width: 690px;
    height: 860px;
    overflow: hidden;
    background: var(--night);
  }
  .label-art {
    position: absolute;
    inset: 0;
    width: 100%;
    height: 100%;
  }
  .label-text {
    position: absolute;
    margin: 0;
    font-family: var(--script);
    font-weight: 400;
    color: var(--ink-light);
    line-height: 1;
    white-space: nowrap;
    text-shadow: 0 1px 2px rgba(0,0,0,0.35);
  }
  .wine-name {
    left: 240px;
    top: 122px;
    font-size: 66px;
  }
  .varietal {
    left: 26px;
    top: 296px;
    font-size: 104px;
  }
  .origin {
    left: 72px;
    top: 725px;
    font-size: 60px;
    line-height: 0.9;
  }
  .origin span { display: block; }
  .origin .country { padding-left: 0; }
</style>
</head>
<body>
<main class="canvas">
  <article class="wine-label">
    <svg class="label-art" viewBox="0 0 655 815" preserveAspectRatio="none" aria-hidden="false">
      <defs>
        <linearGradient id="night-fill" x1="0" y1="0" x2="0" y2="1">
          <stop offset="0" stop-color="var(--night-deep)"/>
          <stop offset="0.5" stop-color="var(--night-soft)"/>
          <stop offset="1" stop-color="var(--night-deep)"/>
        </linearGradient>
        <linearGradient id="gold-fill" x1="0" y1="0" x2="1" y2="1">
          <stop offset="0" stop-color="var(--gold-dark)"/>
          <stop offset="0.45" stop-color="var(--gold-light)"/>
          <stop offset="1" stop-color="var(--gold)"/>
        </linearGradient>
        <linearGradient id="band-fill" x1="0" y1="0" x2="1" y2="0">
          <stop offset="0" stop-color="var(--gold-dark)"/>
          <stop offset="0.5" stop-color="var(--gold)"/>
          <stop offset="1" stop-color="var(--gold-dark)"/>
        </linearGradient>
      </defs>

      <rect class="night-backdrop" width="655" height="815" fill="url(#night-fill)" role="img" aria-label="Dark background with soft scattered circles"/>

      <g class="frame-lines" stroke="var(--gold)" stroke-width="3" fill="none">
        <line x1="630" y1="0" x2="630" y2="650"/>
        <line x1="25" y1="390" x2="25" y2="815"/>
        <line x1="0" y1="270" x2="210" y2="270"/>
        <line x1="200" y1="50" x2="215" y2="110" stroke-width="2"/>
        <line x1="500" y1="60" x2="535" y2="20" stroke-width="2"/>
        <line x1="0" y1="510" x2="75" y2="500" stroke-width="2"/>
        <line x1="365" y1="670" x2="385" y2="815" stroke-width="2"/>
      </g>

      <polygon class="corner-top" points="0,0 262,0 0,310" fill="url(#gold-fill)"/>
      <polygon class="corner-bottom" points="655,628 655,815 368,815" fill="url(#gold-fill)"/>
      <rect class="corner-ornament" x="500" y="705" width="150" height="105" rx="10" fill="var(--gold-light)" opacity="0.35" role="img" aria-label="Gold flower and scroll ornament"/>

      <rect class="name-band" x="210" y="100" width="445" height="90" fill="url(#band-fill)"/>
      <rect class="varietal-band" x="0" y="270" width="365" height="120" fill="url(#band-fill)"/>

      <g class="shooting-star" role="img" aria-label="Gold shooting star with a trail of small stars">
        <polygon points="457,275 592,250 572,315 337,505" fill="url(#gold-fill)"/>
        <rect x="100" y="505" width="230" height="150" rx="20" fill="var(--gold)" opacity="0.22"/>
      </g>
    </svg>

    <h1 class="label-text wine-name">Viento Callado</h1>
    <p class="label-text varietal">Malbec</p>
    <p class="label-text origin"><span class="region">Mendoza</span><span class="country">Argentina</span></p>
  </article>
</main>
</body>
</html>
```